Professional Business Card for Commercial Cleaning Company

We need a business card that represents our commercial janitorial cleaning company and represent several brands for our company so we do not want to highlight the logo too much. We want something that says we are professional.
Notes:No website or address as we have many locations and many websites and companies under our corporate name of "Brightwell Holdings, LLC" . Every time we hand a customer a business card they have contacted us via another brand we own but we don't want to have 21 business cards so we want to not focus on Brightwell Holdings, LLC too much since people will automatically ask "What is Brightwell Holdings, LLC" Example: Noodle Barn and Wrap Dome restaurants are owned by "Zing! Brands" is the corporation name. Same principle here. Except we do not advertise at this time that all of our brands are connected. Hope this helps.
Target Market(s)
Commercial Cleaning
Industry/Entity Type
Janitorial Service
Contact Information for Business Card
Miles Hartwin
Business Development
347-628-9043
sales@brightwellholdingsllc.example
Requirements
Must have
- Logo with contact information, need to be able to easily edit contact info for others in my office.
Nice to have
- Professional Image. Like to see a colorful bold look and a more standard business card look.
Should not have
- Any type of cleaning icons, tools, people or water.

```html
<!DOCTYPE html>
<html lang="en">
<head>
<meta charset="utf-8">
<title>Brightwell Holdings, LLC — Business Card</title>
<link rel="stylesheet" href="https://fonts.googleapis.com/css2?family=Montserrat:wght@700&family=Oswald:wght@500&family=Lato:wght@400&display=swap">
<style>
  :root {
    --page-bg: #1c1c1c;
    --card-bg: #2a2a2a;
    --brand-blue: #2f67a6;
    --accent-green: #5aa83a;
    --text-light: #f2f2f2;
  }
  * { margin: 0; padding: 0; box-sizing: border-box; }
  html, body {
    width: 1200px;
    height: 1200px;
    overflow: hidden;
    background: var(--page-bg);
  }
  .sheet {
    width: 1200px;
    height: 1200px;
    display: flex;
    flex-direction: column;
    align-items: center;
    justify-content: center;
    gap: 40px;
  }
  .card {
    position: relative;
    width: 910px;
    height: 520px;
    background: var(--card-bg);
    box-shadow: 0 10px 30px rgba(0,0,0,0.45);
  }
  .brand-name {
    font-family: "Montserrat", sans-serif;
    font-weight: 700;
    color: var(--brand-blue);
    white-space: nowrap;
  }
  .card--back .brand-name {
    position: absolute;
    top: 50%;
    left: 50%;
    transform: translate(-50%, -50%);
    font-size: 50px;
  }
  .card--front .brand-name {
    position: absolute;
    top: 95px;
    right: 60px;
    font-size: 44px;
  }
  .contact {
    position: absolute;
    left: 64px;
    top: 270px;
  }
  .contact__name {
    font-family: "Oswald", sans-serif;
    font-weight: 500;
    font-size: 50px;
    line-height: 1;
    letter-spacing: 1px;
    text-transform: uppercase;
    color: var(--brand-blue);
  }
  .contact__title {
    font-family: "Lato", sans-serif;
    font-size: 22px;
    color: var(--text-light);
    margin-top: 4px;
  }
  .contact__rule {
    width: 790px;
    height: 2px;
    margin: 10px 0 12px -8px;
    background: linear-gradient(to right, var(--accent-green) 0 300px, var(--brand-blue) 300px 100%);
  }
  .contact__rule-thin { display: none; }
  .contact__line {
    display: flex;
    align-items: center;
    gap: 12px;
    font-family: "Lato", sans-serif;
    font-size: 22px;
    color: var(--text-light);
    margin-bottom: 8px;
  }
  .contact__icon { width: 20px; height: 20px; flex: none; }
</style>
</head>
<body>
  <main class="sheet">
    <section class="card card--back" aria-label="Card back">
      <p class="brand-name">Brightwell Holdings, LLC</p>
    </section>

    <section class="card card--front" aria-label="Card front">
      <p class="brand-name">Brightwell Holdings, LLC</p>
      <div class="contact">
        <h1 class="contact__name">Miles Hartwin</h1>
        <p class="contact__title">Business Development</p>
        <div class="contact__rule"></div>
        <p class="contact__line">
          <svg class="contact__icon" viewBox="0 0 24 24" aria-hidden="true">
            <path fill="#2f67a6" d="M6.6 10.8a15.1 15.1 0 0 0 6.6 6.6l2.2-2.2c.3-.3.7-.4 1-.2 1.1.4 2.3.6 3.6.6.6 0 1 .4 1 1V20c0 .6-.4 1-1 1A17 17 0 0 1 3 4c0-.6.4-1 1-1h3.5c.6 0 1 .4 1 1 0 1.3.2 2.5.6 3.6.1.3 0 .7-.2 1z"/>
          </svg>
          +347-628-9043
        </p>
        <p class="contact__line">
          <svg class="contact__icon" viewBox="0 0 24 24" aria-hidden="true">
            <rect x="2" y="5" width="20" height="14" fill="#2f67a6"/>
            <path d="M2 5l10 8 10-8" fill="none" stroke="#2a2a2a" stroke-width="1.6"/>
          </svg>
          sales@brightwellholdingsllc.example
        </p>
      </div>
    </section>
  </main>
</body>
</html>
```